Business Cards and Print Material
Business cards and print material
I like something that is out of the box. Something different and memorable. I will also need design for envelopes and letter heads. I like the designs so far. Please keep up the good work!
any info or ideas on what you would like ????

```html
<!DOCTYPE html>
<html lang="en">
<head>
<meta charset="utf-8">
<title>Ardent Grove Stationery</title>
<link rel="stylesheet" href="https://fonts.googleapis.com/css2?family=Cinzel:wght@500&family=Open+Sans:wght@400;600&display=swap">
<style>
:root{
  --bg:#eceae6;
  --paper:#ffffff;
  --blue-deep:#1c3a86;
  --blue:#2c58b0;
  --blue-soft:#dde5f4;
  --ink:#2a2f3a;
  --ink-soft:#6b7280;
  --white:#ffffff;
}
*{margin:0;padding:0;box-sizing:border-box}
html,body{width:1200px;height:871px;overflow:hidden;background:var(--bg);font-family:"Open Sans",Arial,sans-serif;color:var(--ink)}
.canvas{position:relative;width:1200px;height:871px}
.sheet{position:absolute;background:var(--paper);box-shadow:0 2px 10px rgba(0,0,0,.12)}
.brand{font-family:"Open Sans",Arial,sans-serif;font-weight:600;letter-spacing:.04em;display:flex;align-items:center;gap:8px}
.brand .dot{width:10px;height:10px;border-radius:50%;background:currentColor}
.person{font-family:"Cinzel",Georgia,serif;font-weight:500;letter-spacing:.06em}
.swirl{position:absolute;background:radial-gradient(ellipse at center,rgba(44,88,176,.12),rgba(44,88,176,0) 70%)}

/* Letterhead */
.letterhead{left:60px;top:73px;width:560px;height:725px}
.letterhead .band{position:absolute;left:0;top:0;width:100%;height:130px;background:linear-gradient(100deg,var(--blue-deep),var(--blue))}
.letterhead .band .brand{position:absolute;left:36px;top:46px;color:var(--white);font-size:26px}
.letterhead .band .person{position:absolute;right:36px;top:34px;color:var(--white);font-size:17px}
.letterhead .band .title{position:absolute;right:36px;top:58px;color:var(--blue-soft);font-size:10px}
.letterhead .sidebar{position:absolute;left:36px;top:170px;width:140px;font-size:9.5px;line-height:1.6;color:var(--ink-soft)}
.letterhead .sidebar p{margin-bottom:14px}
.letterhead .sidebar b{color:var(--blue-deep);font-weight:600}
.letterhead .body{position:absolute;left:200px;top:170px;width:320px;font-size:11px;line-height:1.7}
.letterhead .body p{margin-bottom:14px}
.letterhead .sign .name{font-weight:600;color:var(--blue-deep);margin-top:34px}
.letterhead .sign .role{color:var(--ink-soft)}
.letterhead .swirl{left:160px;top:470px;width:380px;height:200px}

/* Envelope */
.envelope{left:660px;top:73px;width:480px;height:208px}
.envelope .brand{position:absolute;left:24px;top:22px;color:var(--blue-deep);font-size:20px}
.envelope .person{position:absolute;left:24px;top:60px;color:var(--blue-deep);font-size:12px}
.envelope .return{position:absolute;left:24px;top:80px;font-size:9px;line-height:1.5;color:var(--ink-soft)}
.envelope .stamp{position:absolute;right:20px;top:18px;width:38px;height:46px;background:linear-gradient(#c9c4b8,#a8a294);border:2px solid #f4f1ea}
.envelope .swirl{left:140px;top:110px;width:320px;height:90px}

/* Cards */
.card{width:340px;height:194px;background:linear-gradient(110deg,var(--blue-deep),var(--blue));color:var(--white);overflow:hidden}
.card-front{left:660px;top:330px}
.card-back{left:800px;top:560px}
.card-front .brand{position:absolute;left:22px;top:22px;font-size:22px}
.card-front .person{position:absolute;left:22px;top:92px;font-size:14px}
.card-front .title{position:absolute;left:22px;top:112px;font-size:8.5px;color:var(--blue-soft)}
.card-front .contact{position:absolute;left:22px;top:134px;font-size:8px;line-height:1.5;color:var(--blue-soft)}
.card-front .contact b{display:inline-block;width:40px;font-weight:600;color:var(--white)}
.card-back .brand{position:absolute;left:0;right:0;top:80px;justify-content:center;font-size:26px}
.card .swirl{left:150px;top:40px;width:240px;height:160px;background:radial-gradient(ellipse at center,rgba(255,255,255,.14),rgba(255,255,255,0) 70%)}
</style>
</head>
<body>
<main class="canvas">

  <section class="sheet letterhead">
    <header class="band">
      <div class="brand"><span class="dot"></span>Ardent Grove</div>
      <div class="person">Tessa Wilde</div>
      <div class="title">Director of Operations</div>
    </header>
    <aside class="sidebar">
      <p>4410 Harbor Row<br>Suite 212<br>Lakemont, OR 97034</p>
      <p><b>Phone</b> 555 014 2231<br><b>Cell</b> 555 014 7780<br><b>Fax</b> 555 014 2232</p>
      <p>tessa@ardentgrove.example</p>
    </aside>
    <div class="swirl" role="img" aria-label="Faint blue looping line decoration"></div>
    <article class="body">
      <p>Dear Mrs. Holloway,</p>
      <p>Thank you for meeting with our team last week. We enjoyed learning about your plans for the coming season and look forward to helping you shape them.</p>
      <p>Enclosed you will find a summary of the services we discussed, along with a proposed schedule. Please review it at your convenience and share any questions.</p>
      <p>We are grateful for your trust and are ready to begin whenever you are.</p>
      <div class="sign">
        <p>Sincerely,</p>
        <div class="name">Tessa Wilde</div>
        <div class="role">Director of Operations</div>
      </div>
    </article>
  </section>

  <section class="sheet envelope">
    <div class="brand"><span class="dot"></span>Ardent Grove</div>
    <div class="person">Tessa Wilde</div>
    <div class="return">4410 Harbor Row<br>Suite 212<br>Lakemont, OR 97034</div>
    <div class="stamp" role="img" aria-label="Postage stamp"></div>
    <div class="swirl" role="img" aria-label="Faint blue looping line decoration"></div>
  </section>

  <section class="sheet card card-front">
    <div class="swirl" role="img" aria-label="Soft light looping line decoration"></div>
    <div class="brand"><span class="dot"></span>Ardent Grove</div>
    <div class="person">Tessa Wilde</div>
    <div class="title">Director of Operations</div>
    <div class="contact">
      <b>Phone</b>555 014 2231<br>
      <b>Cell</b>555 014 7780<br>
      <b>Email</b>tessa@ardentgrove.example
    </div>
  </section>

  <section class="sheet card card-back">
    <div class="swirl" role="img" aria-label="Soft light looping line decoration"></div>
    <div class="brand"><span class="dot"></span>Ardent Grove</div>
  </section>

</main>
</body>
</html>
```